exquisite label design for foam cleanser

Kindly invite you to design bottle label (102 mm*64 mm) for our product, a kind of foam cleanser for wearable aligners. The color of bottle and liquid inside are both clear, but the foam pump is white. You could download the pic of bottle among the uploaded files. I have no KV of our website or posters to supply you, except the logo file attached. Content on the label is attached too. Please check it. I wish the label would make our product look high-end and reliable. And it would be better if you could give some advice on paper material and special requirements for printing, related to your design. I value the texture of label too, because I think that stands for the quality of products. No color limitation for the use of our logo, and please ignore the Chinese characters in our logo, they are not in our plan.
Target Market(s)
16-35 female, orthodontic patients.
Colors
Designer to choose colors to be used in the design.
Look and feel
Each slider illustrates characteristics of the customer's brand and the style your logo design should communicate.

```html
<!DOCTYPE html>
<html lang="en">
<head>
<meta charset="utf-8">
<title>Lumora Aligner Cleansing Foam Label</title>
<link rel="stylesheet" href="https://fonts.googleapis.com/css2?family=Jost:wght@400;500;600&family=Noto+Sans+SC:wght@400&display=swap">
<style>
  :root {
    --page: #f3f4f5;
    --label: #eceef0;
    --mint: #a3dcc8;
    --navy: #1f2c86;
    --sky: #3a8fce;
    --brand: #2b7fd4;
    --white: #ffffff;
  }
  html, body {
    margin: 0;
    width: 1200px;
    height: 1026px;
    overflow: hidden;
    background: var(--page);
  }
  .label {
    position: absolute;
    left: 390px;
    top: 33px;
    width: 420px;
    height: 960px;
    background: var(--label);
    display: flex;
    box-shadow: 0 0 0 1px rgba(0,0,0,0.04);
  }
  .label__band {
    width: 118px;
    background: var(--mint);
    display: flex;
    align-items: flex-start;
    justify-content: center;
  }
  .label__band-text {
    margin-top: 230px;
    writing-mode: vertical-rl;
    text-orientation: sideways;
    transform: rotate(180deg);
    font-family: "Noto Sans SC", sans-serif;
    font-size: 34px;
    letter-spacing: 9px;
    color: var(--white);
    white-space: nowrap;
  }
  .label__body {
    flex: 1;
    position: relative;
    font-family: "Jost", sans-serif;
  }
  .brand-name {
    position: absolute;
    left: 20px;
    top: 150px;
    margin: 0;
    font-family: "Jost", sans-serif;
    font-weight: 600;
    font-size: 54px;
    letter-spacing: 1px;
    color: var(--brand);
  }
  .headline {
    position: absolute;
    left: 20px;
    top: 380px;
    margin: 0;
    font-size: 40px;
    line-height: 54px;
    text-transform: uppercase;
  }
  .headline__strong { display: block; font-weight: 600; color: var(--navy); }
  .headline__soft { display: block; font-weight: 400; color: var(--sky); }
  .flavor {
    position: absolute;
    left: 20px;
    top: 662px;
    padding: 6px 14px;
    border: 2px solid var(--sky);
    font-size: 25px;
    font-weight: 500;
    letter-spacing: 2px;
    color: var(--sky);
  }
  .volume {
    position: absolute;
    left: 20px;
    top: 788px;
    margin: 0;
    font-size: 22px;
    letter-spacing: 2px;
    color: var(--navy);
  }
</style>
</head>
<body>
  <main class="label">
    <div class="label__band">
      <span class="label__band-text">隐形牙套清洁泡沫</span>
    </div>
    <div class="label__body">
      <h1 class="brand-name">Lumora</h1>
      <h2 class="headline">
        <span class="headline__strong">Deep</span>
        <span class="headline__strong">Cleaning &amp;</span>
        <span class="headline__soft">Lasting</span>
        <span class="headline__soft">Freshness</span>
      </h2>
      <div class="flavor">MINT FLAVOR</div>
      <p class="volume">1.69 Fl Oz / 50ml</p>
    </div>
  </main>
</body>
</html>
```